Ashworth Web Design Project

I need the front page and an internal page designed for this client's website. The logo is attached. Obviously the colors have to go with and/or work with the logo colors. I also attached a very rough brochure layout to help you see the direction we're going in with print materials. The rough site map is also attached. I see a slider on the homepage, the art for which I may come back to you to create. This clinic is in a very high end Dallas neighborhood. The hook is that it's a primary care and urgent facility with convenient hours.

I don't know how much this impacts your design, but this will be a Wordpress site and I'm using a framework called Struxo (struxo-demo.example). If Struxo proves to be inflexible, I'll have to get a template that allows me to execute your design.

This site (http://oakbendcareclinic.example) has the type and quality of content I will eventually have on the Ashworth site.

I just revised the brief for this project. I added the site map and added details to the overview and the "Must Have" section. Thank you for revisiting the brief. 

Reason: Christmas was a bad time to end it.

Target Market(s)

Women 25-54 with children living at home, income over $150k/year

Industry/Entity Type

Clinic

Requirements
Must have
• Masthead incorporating the logo
Followed by the primary nav
Slider on the home page below that
Dual nav - 1 with the nav in the attached site map
2 secondary nav with areas of healthcare
There will three blocks under the nav
1. It's about time (with a small blurb less than 50 words.
2. It's about choices (with small blurb)
3. It's about you (with small blurb)
Three footer blocks
patient check in link on every page
"No appointment? No problem" icon on every page

```html
<!DOCTYPE html>
<html lang="en">
<head>
<meta charset="utf-8">
<title>Ashworth Medical — Home</title>
<link href="https://fonts.googleapis.com/css2?family=Noto+Sans:wght@400;700&family=PT+Sans:wght@400;700&family=Oswald:wght@500;600&display=swap" rel="stylesheet">
<style>
:root{
  --green:#22b05a;
  --green-dark:#1c9a4d;
  --blue:#0b5c9e;
  --blue-logo:#1a5fa8;
  --navy:#063b63;
  --navy-deep:#053256;
  --gray-bg:#ececec;
  --text:#222;
  --card-text:#333;
  --red:#d10b1a;
  --white:#fff;
}
*{margin:0;padding:0;box-sizing:border-box}
html,body{width:1164px;height:1200px;overflow:hidden}
body{position:relative;background:var(--white);font-family:"Noto Sans",sans-serif;color:var(--text)}
.abs{position:absolute}

/* top bar */
.topbar{left:0;top:0;width:1164px;height:35px;background:var(--green)}
.social{top:4px;height:27px;display:flex;gap:10px;left:875px}
.social span{width:27px;height:27px;border-radius:4px;background:rgba(255,255,255,.85)}

/* masthead */
.brand{left:175px;top:62px;display:flex;align-items:center;gap:12px}
.brand-mark{width:58px;height:58px;border-radius:50%;background:var(--blue-logo)}
.brand-name{font-family:"PT Sans",sans-serif;font-weight:700;font-size:38px;line-height:40px;color:var(--blue-logo);letter-spacing:-.5px}
.brand-tag{font-family:"PT Sans",sans-serif;font-weight:700;font-size:13px;color:#1d3f66;margin-top:0;display:flex;align-items:center;gap:5px}
.brand-tag i{display:block;width:34px;height:1.5px;background:#1d3f66}
.account{left:773px;top:59px;width:218px;height:32px;background:#8a8a8a;border-radius:3px;display:flex;align-items:center;justify-content:space-around;color:var(--white);font-family:"PT Sans",sans-serif;font-size:12.5px;padding:0 6px}

/* nav */
.mainnav{left:0;top:147px;width:1164px;height:35px;background:var(--blue);border-bottom:1px solid #4d8cc4}
.mainnav ul{list-style:none;display:flex;gap:0;position:absolute;left:185px;top:0;height:35px;align-items:center}
.mainnav li{font-family:"PT Sans",sans-serif;font-weight:700;font-size:12px;letter-spacing:.8px;color:var(--white);margin-right:25px}

/* slider */
.slider-band{left:0;top:182px;width:1164px;height:294px;background:#233f8c}
.slider{left:172px;top:182px;width:819px;height:294px;border:2px solid var(--green);background:linear-gradient(100deg,#8fae5a 0%,#6f9143 35%,#4f7030 65%,#3c5a25 100%)}
.care-menu{left:320px;top:184px;width:167px;height:208px;background:rgba(40,80,120,.62);padding:9px 0 0 10px}
.care-menu li{list-style:none;font-family:"PT Sans",sans-serif;font-size:11px;color:var(--white);height:28.5px;border-bottom:1px dashed rgba(255,255,255,.45);width:137px;display:flex;align-items:center;gap:4px}
.care-menu li:last-child{border-bottom:none}
.care-menu svg{flex:none}
.slide-title{left:655px;top:204px;width:320px;font-family:"PT Sans",sans-serif;font-weight:700;font-size:18.5px;line-height:25px;color:var(--white);text-shadow:0 1px 2px rgba(0,0,0,.5)}
.slide-btn{left:651px;top:285px;width:106px;height:24px;border-radius:4px;background:linear-gradient(#2c5ec4,#173f95);border:1px solid #8fb0e8;color:var(--white);font-size:11px;text-align:center;line-height:22px}
.arrow{top:310px}
.pager{left:905px;top:453px;display:flex;gap:4px}
.pager span{width:13px;height:13px;border:1px solid #ccc;background:#444;color:#fff;font-size:8.5px;text-align:center;line-height:11px}
.pager span.on{background:#fff;color:#222}

/* content */
.content-bg{left:0;top:476px;width:1164px;height:468px;background:var(--gray-bg)}
.column{left:172px;top:476px;width:819px;height:468px;background:linear-gradient(#e6e6e6 0,#fff 70px,#fff 100%)}
.welcome{left:190px;top:497px;font-size:19px;letter-spacing:.6px;font-weight:400;color:#111}
.intro{left:190px;top:531px;width:780px;font-size:10.6px;line-height:16.4px;letter-spacing:.25px}
.more{left:896px;top:589px;font-size:8.5px;font-weight:700;color:var(--red);display:flex;align-items:center;gap:3px;letter-spacing:.3px}
.card{top:614px;width:248px;height:312px;border:1px solid #e2e2e2;background:var(--white)}
.card-photo{width:100%;height:170px}
.card-band{height:26px;background:linear-gradient(#5cc77e,var(--green-dark));color:var(--white);font-family:"Oswald",sans-serif;font-weight:600;font-size:14.5px;letter-spacing:.6px;text-align:center;line-height:26px;text-shadow:0 1px 1px rgba(0,0,0,.35)}
.card-text{padding:18px 9px 0 9px;font-size:10.6px;line-height:14.6px;letter-spacing:.3px;color:var(--card-text)}

/* footer */
.footer{left:0;top:944px;width:1164px;height:220px;background:var(--navy)}
.footer h3{position:absolute;font-weight:400;font-size:17.5px;color:var(--white)}
.video-thumb{left:191px;top:990px;width:193px;height:118px;border:3px solid #bdbdbd;background:linear-gradient(120deg,#8a8776,#5d5a48 55%,#9b9887);box-shadow:2px 3px 4px rgba(0,0,0,.45)}
.post{left:465px;display:flex;gap:4px}
.post-date{width:33px;height:40px;background:var(--white);text-align:center}
.post-date b{display:block;background:#e00;color:#222;font-family:Georgia,serif;font-size:12.5px;height:22px;line-height:24px;font-weight:700}
.post-date span{display:block;color:var(--red);font-family:Georgia,serif;font-size:13px;line-height:18px}
.post-body{font-size:11px;color:#dfe8f0;line-height:15.5px}
.post-body em{display:block;color:#f0a0a0;font-style:italic;font-size:10.5px}
.post-body small{display:block;color:var(--white);font-size:8.5px;font-weight:700}
.contact{left:745px;top:986px;font-size:11px;line-height:14.8px;letter-spacing:.45px;color:#dfe8f0}
.copyright{left:0;top:1164px;width:1164px;height:36px;background:var(--navy);border-top:1px solid #3f78a8;text-align:center;font-size:9px;line-height:34px;color:#b9c9d8}
</style>
</head>
<body>

<div class="abs topbar"></div>
<div class="abs social" aria-label="Social links">
  <span role="img" aria-label="Social link"></span>
  <span role="img" aria-label="Social link"></span>
  <span role="img" aria-label="Video channel link"></span>
</div>

<header>
  <div class="abs brand">
    <div class="brand-mark"></div>
    <div>
      <div class="brand-name">AshworthMedical</div>
      <div class="brand-tag"><i></i>Immediate Family and Personal Care<i></i></div>
    </div>
  </div>
  <div class="abs account"><span>Register</span><span>|</span><span>Log In</span><span>|</span><span>Blog</span></div>
</header>

<nav class="abs mainnav">
  <ul><li>HOME</li><li>ABOUT US</li><li>SERVICES</li><li>STAFF</li><li>INSURANCE</li><li>VIDEOS</li><li>CONTACT US</li></ul>
</nav>

<section>
  <div class="abs slider-band"></div>
  <div class="abs slider" role="img" aria-label="Slide photo: a smiling father and young son lying on green grass outdoors"></div>
  <ul class="abs care-menu">
    <li><svg width="7" height="10"><path d="M1 1l4 4-4 4" stroke="#e3131f" stroke-width="2" fill="none"/></svg>Immediate Care</li>
    <li><svg width="7" height="10"><path d="M1 1l4 4-4 4" stroke="#e3131f" stroke-width="2" fill="none"/></svg>Allergies</li>
    <li><svg width="7" height="10"><path d="M1 1l4 4-4 4" stroke="#e3131f" stroke-width="2" fill="none"/></svg>Primary Care</li>
    <li><svg width="7" height="10"><path d="M1 1l4 4-4 4" stroke="#e3131f" stroke-width="2" fill="none"/></svg>Women's Health</li>
    <li><svg width="7" height="10"><path d="M1 1l4 4-4 4" stroke="#e3131f" stroke-width="2" fill="none"/></svg>Medical Spa Treatments</li>
    <li><svg width="7" height="10"><path d="M1 1l4 4-4 4" stroke="#e3131f" stroke-width="2" fill="none"/></svg>Men's Health</li>
    <li><svg width="7" height="10"><path d="M1 1l4 4-4 4" stroke="#e3131f" stroke-width="2" fill="none"/></svg>Weight Loss</li>
  </ul>
  <div class="abs slide-title">Lorem ipsum dolor sit amet consec-tetuer adipscing elit. Nam cursus. Morbi ut mi. Lorem ipsum dolor sit</div>
  <div class="abs slide-btn">Learn more</div>
  <svg class="abs arrow" style="left:183px" width="30" height="40"><path d="M24 3L8 20l16 17" stroke="#fff" stroke-width="6" fill="none"/></svg>
  <svg class="abs arrow" style="left:948px" width="30" height="40"><path d="M6 3l16 17-16 17" stroke="#fff" stroke-width="6" fill="none"/></svg>
  <div class="abs pager"><span>1</span><span class="on">2</span><span>3</span><span>4</span></div>
</section>

<main>
  <div class="abs content-bg"></div>
  <div class="abs column"></div>
  <h1 class="abs welcome">Welcome to AshworthFamilyMedical</h1>
  <p class="abs intro">Lorem ipsum dolor sit amet, consectetuer adipiscing elit. Nam cursus. Morbi ut mi. Nullam enim leo, egestas id, condimentum at, laoreet mattis, massa. Sed eleifend nonummy diam. Praesent mauris ante, elementum et, bibendum at, posuere sit amet, nibh. Duis tincidunt lectus quis dui viverra vestibulum. Suspendisse vulputate aliquam dui. Nulla elementum dui ut augue. Aliquam vehicula mi at mauris. Maecenas</p>
  <div class="abs more">Learn more <svg width="6" height="9"><path d="M1 1l3.5 3.5L1 8" stroke="#d10b1a" stroke-width="2" fill="none"/></svg></div>

  <article class="abs card" style="left:190px">
    <div class="card-photo" role="img" aria-label="Photo: a smiling family of four outdoors" style="background:linear-gradient(160deg,#c9d9a8,#a7b98a 50%,#e0d2bd)"></div>
    <div class="card-band">IT'S ABOUT TIME</div>
    <p class="card-text">Lorem ipsum dolor sit amet consectetuer adipiscing elit. Nam cursus. Morbi ut mi Nullam enim leo, egestas id condimentum at, laoreet mattis, massa. Sed eleifend nonummy diam. Praesent mauris ante, elementum et bibendum atposuer&nbsp; amet.</p>
  </article>
  <article class="abs card" style="left:457px">
    <div class="card-photo" role="img" aria-label="Photo: a mother hugging her young daughter in a summer field" style="background:linear-gradient(160deg,#c79a4c,#d9b774 50%,#b48d44)"></div>
    <div class="card-band">IT'S ABOUT YOU</div>
    <p class="card-text">Lorem ipsum dolor sit amet consectetuer adipiscing elit. Nam cursus. Morbi ut mi Nullam enim leo, egestas id condimentum at, laoreet mattis, massa. Sed eleifend nonummy diam. Praesent mauris ante, elementum et bibendum atposuer&nbsp; amet.</p>
  </article>
  <article class="abs card" style="left:723px">
    <div class="card-photo" role="img" aria-label="Photo: parents and two children playing together on a bed" style="background:linear-gradient(160deg,#dfe6ea,#c9c3b8 55%,#a99d8e)"></div>
    <div class="card-band">IT'S ABOUT CHOICES</div>
    <p class="card-text">Lorem ipsum dolor sit amet consectetuer adipiscing elit. Nam cursus. Morbi ut mi Nullam enim leo, egestas id condimentum at, laoreet mattis, massa. Sed eleifend nonummy diam. Praesent mauris ante, elementum et bibendum atposuer&nbsp; amet.</p>
  </article>
</main>

<footer>
  <div class="abs footer">
    <h3 style="left:190px;top:15px">Video</h3>
    <h3 style="left:465px;top:15px">Blog</h3>
    <h3 style="left:741px;top:15px">Contact Us</h3>
  </div>
  <div class="abs video-thumb" role="img" aria-label="Video still: a couple outdoors by rocks"></div>
  <svg class="abs" style="left:260px;top:1023px" width="56" height="42"><rect width="56" height="42" rx="4" fill="rgba(40,40,40,.75)"/><path d="M22 11l16 10-16 10z" fill="#ddd"/></svg>

  <div class="abs post" style="top:993px">
    <div class="post-date"><b>Dec</b><span>13</span></div>
    <div class="post-body">Lorem ipsum dolor sit amet<em>Lorem ipsum,</em><small>13/12/2012</small></div>
  </div>
  <div class="abs post" style="top:1050px">
    <div class="post-date"><b>Dec</b><span>12</span></div>
    <div class="post-body">Lorem ipsum dolor sit amet<em>Lorem ipsum ,</em><small>12/12/2012</small></div>
  </div>
  <div class="abs post" style="top:1108px">
    <div class="post-date"><b>Dec</b><span>07</span></div>
    <div class="post-body">Lorem ipsum dolor sit amet<em>Lorem ipsum,</em><small>07/12/2012</small></div>
  </div>

  <address class="abs contact" style="font-style:normal">
    AshworthFamilyMedical<br>
    4120 Linden Park Ave (at Elm Rd) Ste<br>
    210, Dallas, TX 75230<br><br>
    Tel: (555) 014 2200<br>
    Fax: (555) 014 2201<br>
    E-mail: info@ashworthfamilymedical.example
  </address>

  <div class="abs copyright">Copyright 2012 &nbsp;AshworthFamilyMedical. All rights reserved.</div>
</footer>

</body>
</html>
```